label design for cannabis

label template 4"x5.5" for a Massachusetts cannabis beverage product. labels will be transparent and placed on a blue (pantone 306C) bag.
https://www.fravostones.com/

Target Market(s)

cannabis customers in MA, 21+

Industry/Entity Type

cannabis consumer product

Font styles to use
Other font styles liked:
• DIN

Colors
0094D4
00A9DD
6FCCEA
C7EBF8
E9F6FB

Requirements
Must have
• label design with fravo logo, flavor (lemon, lime, plain, and coffee). 306C pantone for background and 11-0601 TCX for text. font=DINackground.
Nice to have
• tray icon, illustrated ice cubes in white (clear), yellow (lemon), green (lime) and brown (coffee)
Should not have
• no cartoonish characters

```html
<!DOCTYPE html>
<html lang="en">
<head>
<meta charset="utf-8">
<title>fravo infused ice cubes – label set</title>
<link rel="stylesheet" href="https://fonts.googleapis.com/css2?family=Barlow:wght@500;600&family=Barlow+Condensed:wght@500;600&display=swap">
<style>
  :root {
    --page: #ffffff;
    --label-blue: #00b8e2;
    --text-white: #ffffff;
    --accent-yellow: #e8ee1a;
    --warn-red: #d8242a;
    --ink: #111111;
    --coffee-a: #f5b27a; --coffee-b: #e88a3c;
    --lemon-a: #f6f36a;  --lemon-b: #d9d80a;
    --lime-a: #c6f0a0;   --lime-b: #86cf55;
    --plain-a: #e8eef8;  --plain-b: #b4c2dc;
  }
  * { box-sizing: border-box; margin: 0; padding: 0; }
  html, body { width: 895px; height: 1200px; overflow: hidden; background: var(--page); }
  .sheet { position: relative; width: 895px; height: 1200px; }

  .label {
    position: absolute; width: 359px; height: 494px;
    background: var(--label-blue); color: var(--text-white);
    font-family: "Barlow", sans-serif; overflow: hidden;
  }
  .label--coffee { left: 65px;  top: 63px; }
  .label--lemon  { left: 475px; top: 63px; }
  .label--lime   { left: 61px;  top: 604px; }
  .label--plain  { left: 475px; top: 604px; }

  .label__url {
    position: absolute; top: 13px; left: 0; width: 100%; text-align: center;
    font-size: 14px; line-height: 18px; font-weight: 600; letter-spacing: 0.32em;
  }
  .label__brand {
    position: absolute; top: 46px; left: 0; width: 100%; text-align: center;
    font-family: "Barlow Condensed", sans-serif; font-weight: 600;
    font-size: 124px; line-height: 124px; letter-spacing: -0.01em;
  }
  .label__tagline {
    position: absolute; top: 156px; left: 0; width: 100%; text-align: center;
    font-family: "Barlow Condensed", sans-serif; font-weight: 500;
    font-size: 30px; line-height: 36px;
  }
  .label__cubes {
    position: absolute; left: 66px; top: 204px; width: 228px; height: 138px;
    border-radius: 8px;
  }
  .label--coffee .label__cubes { background: linear-gradient(160deg, var(--coffee-a), var(--coffee-b)); }
  .label--lemon  .label__cubes { background: linear-gradient(160deg, var(--lemon-a), var(--lemon-b)); }
  .label--lime   .label__cubes { background: linear-gradient(160deg, var(--lime-a), var(--lime-b)); }
  .label--plain  .label__cubes { background: linear-gradient(160deg, var(--plain-a), var(--plain-b)); }

  .label__flavor {
    position: absolute; top: 358px; left: 112px; width: 138px; height: 34px;
    border-top: 1.5px solid rgba(255,255,255,0.8);
    border-bottom: 1.5px solid rgba(255,255,255,0.8);
    display: flex; align-items: center; justify-content: center;
    font-size: 21px; line-height: 1; font-weight: 600; letter-spacing: 0.38em; padding-left: 0.38em;
  }
  .label--lemon .label__flavor { color: var(--accent-yellow); }

  .label__thc { position: absolute; left: 17px; top: 428px; width: 50px; text-align: center; }
  .label__thc svg { display: block; margin: 0 auto; }
  .label__thc-text {
    font-family: "Barlow Condensed", sans-serif; font-weight: 600; font-size: 9.5px;
    line-height: 11px; white-space: nowrap; margin-top: 3px;
  }

  .label__dose { position: absolute; left: 126px; top: 434px; width: 110px; text-align: center; }
  .label__dose svg { display: block; margin: 0 auto; }
  .label__dose-text {
    color: var(--accent-yellow); font-weight: 600; font-size: 12px; line-height: 14px;
    letter-spacing: 0.02em; margin-top: 4px; white-space: nowrap;
  }

  .label__kids { position: absolute; left: 308px; top: 433px; width: 40px; height: 40px; }
</style>
</head>
<body>
<main class="sheet">

  <section class="label label--coffee">
    <p class="label__url">www.fravostones.com</p>
    <h1 class="label__brand">fravo</h1>
    <p class="label__tagline">infused ice cubes</p>
    <div class="label__cubes" role="img" aria-label="Stack of four orange coffee-flavoured ice cubes"></div>
    <p class="label__flavor">COFFEE</p>
    <div class="label__thc">
      <svg width="40" height="36" viewBox="0 0 40 36"><path d="M20 2 L38 34 H2 Z" fill="#fff" stroke="#d8242a" stroke-width="3" stroke-linejoin="round"/><circle cx="20" cy="23" r="5" fill="#111"/></svg>
      <p class="label__thc-text">CONTAINS THC</p>
    </div>
    <div class="label__dose">
      <svg width="108" height="26" viewBox="0 0 108 26" fill="none" stroke="#e8ee1a" stroke-width="1.4">
        <rect x="1" y="1" width="106" height="7"/>
        <text x="54" y="6.8" fill="#e8ee1a" stroke="none" font-family="Barlow, sans-serif" font-size="6" letter-spacing="1.2" text-anchor="middle">50MG PER TRAY</text>
        <path d="M4 10 H18 L15 24 H7 Z M21 10 H35 L32 24 H24 Z M38 10 H52 L49 24 H41 Z M56 10 H70 L67 24 H59 Z M73 10 H87 L84 24 H76 Z M90 10 H104 L101 24 H93 Z"/>
      </svg>
      <p class="label__dose-text">50MG PER TRAY</p>
    </div>
    <svg class="label__kids" viewBox="0 0 40 40">
      <polygon points="12,1 28,1 39,12 39,28 28,39 12,39 1,28 1,12" fill="#fff" stroke="#d8242a" stroke-width="3"/>
      <text x="20" y="18" font-family="Barlow Condensed, sans-serif" font-weight="600" font-size="9" fill="#111" text-anchor="middle">NOT SAFE</text>
      <text x="20" y="27" font-family="Barlow Condensed, sans-serif" font-weight="600" font-size="9" fill="#111" text-anchor="middle">FOR KIDS</text>
    </svg>
  </section>

  <section class="label label--lemon">
    <p class="label__url">www.fravostones.com</p>
    <h2 class="label__brand">fravo</h2>
    <p class="label__tagline">infused ice cubes</p>
    <div class="label__cubes" role="img" aria-label="Stack of four yellow lemon-flavoured ice cubes"></div>
    <p class="label__flavor">LEMON</p>
    <div class="label__thc">
      <svg width="40" height="36" viewBox="0 0 40 36"><path d="M20 2 L38 34 H2 Z" fill="#fff" stroke="#d8242a" stroke-width="3" stroke-linejoin="round"/><circle cx="20" cy="23" r="5" fill="#111"/></svg>
      <p class="label__thc-text">CONTAINS THC</p>
    </div>
    <div class="label__dose">
      <svg width="108" height="26" viewBox="0 0 108 26" fill="none" stroke="#e8ee1a" stroke-width="1.4">
        <rect x="1" y="1" width="106" height="7"/>
        <text x="54" y="6.8" fill="#e8ee1a" stroke="none" font-family="Barlow, sans-serif" font-size="6" letter-spacing="1.2" text-anchor="middle">50MG PER TRAY</text>
        <path d="M4 10 H18 L15 24 H7 Z M21 10 H35 L32 24 H24 Z M38 10 H52 L49 24 H41 Z M56 10 H70 L67 24 H59 Z M73 10 H87 L84 24 H76 Z M90 10 H104 L101 24 H93 Z"/>
      </svg>
      <p class="label__dose-text">50MG PER TRAY</p>
    </div>
    <svg class="label__kids" viewBox="0 0 40 40">
      <polygon points="12,1 28,1 39,12 39,28 28,39 12,39 1,28 1,12" fill="#fff" stroke="#d8242a" stroke-width="3"/>
      <text x="20" y="18" font-family="Barlow Condensed, sans-serif" font-weight="600" font-size="9" fill="#111" text-anchor="middle">NOT SAFE</text>
      <text x="20" y="27" font-family="Barlow Condensed, sans-serif" font-weight="600" font-size="9" fill="#111" text-anchor="middle">FOR KIDS</text>
    </svg>
  </section>

  <section class="label label--lime">
    <p class="label__url">www.fravostones.com</p>
    <h2 class="label__brand">fravo</h2>
    <p class="label__tagline">infused ice cubes</p>
    <div class="label__cubes" role="img" aria-label="Stack of four green lime-flavoured ice cubes"></div>
    <p class="label__flavor">LIME</p>
    <div class="label__thc">
      <svg width="40" height="36" viewBox="0 0 40 36"><path d="M20 2 L38 34 H2 Z" fill="#fff" stroke="#d8242a" stroke-width="3" stroke-linejoin="round"/><circle cx="20" cy="23" r="5" fill="#111"/></svg>
      <p class="label__thc-text">CONTAINS THC</p>
    </div>
    <div class="label__dose">
      <svg width="108" height="26" viewBox="0 0 108 26" fill="none" stroke="#e8ee1a" stroke-width="1.4">
        <rect x="1" y="1" width="106" height="7"/>
        <text x="54" y="6.8" fill="#e8ee1a" stroke="none" font-family="Barlow, sans-serif" font-size="6" letter-spacing="1.2" text-anchor="middle">50MG PER TRAY</text>
        <path d="M4 10 H18 L15 24 H7 Z M21 10 H35 L32 24 H24 Z M38 10 H52 L49 24 H41 Z M56 10 H70 L67 24 H59 Z M73 10 H87 L84 24 H76 Z M90 10 H104 L101 24 H93 Z"/>
      </svg>
      <p class="label__dose-text">50MG PER TRAY</p>
    </div>
    <svg class="label__kids" viewBox="0 0 40 40">
      <polygon points="12,1 28,1 39,12 39,28 28,39 12,39 1,28 1,12" fill="#fff" stroke="#d8242a" stroke-width="3"/>
      <text x="20" y="18" font-family="Barlow Condensed, sans-serif" font-weight="600" font-size="9" fill="#111" text-anchor="middle">NOT SAFE</text>
      <text x="20" y="27" font-family="Barlow Condensed, sans-serif" font-weight="600" font-size="9" fill="#111" text-anchor="middle">FOR KIDS</text>
    </svg>
  </section>

  <section class="label label--plain">
    <p class="label__url">www.fravostones.com</p>
    <h2 class="label__brand">fravo</h2>
    <p class="label__tagline">infused ice cubes</p>
    <div class="label__cubes" role="img" aria-label="Stack of four clear plain ice cubes"></div>
    <p class="label__flavor">PLAIN</p>
    <div class="label__thc">
      <svg width="40" height="36" viewBox="0 0 40 36"><path d="M20 2 L38 34 H2 Z" fill="#fff" stroke="#d8242a" stroke-width="3" stroke-linejoin="round"/><circle cx="20" cy="23" r="5" fill="#111"/></svg>
      <p class="label__thc-text">CONTAINS THC</p>
    </div>
    <div class="label__dose">
      <svg width="108" height="26" viewBox="0 0 108 26" fill="none" stroke="#e8ee1a" stroke-width="1.4">
        <rect x="1" y="1" width="106" height="7"/>
        <text x="54" y="6.8" fill="#e8ee1a" stroke="none" font-family="Barlow, sans-serif" font-size="6" letter-spacing="1.2" text-anchor="middle">50MG PER TRAY</text>
        <path d="M4 10 H18 L15 24 H7 Z M21 10 H35 L32 24 H24 Z M38 10 H52 L49 24 H41 Z M56 10 H70 L67 24 H59 Z M73 10 H87 L84 24 H76 Z M90 10 H104 L101 24 H93 Z"/>
      </svg>
      <p class="label__dose-text">50MG PER TRAY</p>
    </div>
    <svg class="label__kids" viewBox="0 0 40 40">
      <polygon points="12,1 28,1 39,12 39,28 28,39 12,39 1,28 1,12" fill="#fff" stroke="#d8242a" stroke-width="3"/>
      <text x="20" y="18" font-family="Barlow Condensed, sans-serif" font-weight="600" font-size="9" fill="#111" text-anchor="middle">NOT SAFE</text>
      <text x="20" y="27" font-family="Barlow Condensed, sans-serif" font-weight="600" font-size="9" fill="#111" text-anchor="middle">FOR KIDS</text>
    </svg>
  </section>

</main>
</body>
</html>
```